Corporate Identity Pack - LetterHead, Business Card, Envelope

We are looking for a clean, professional, and visually connected corporate identity set for our company "VELTA HOME" (Cleaning, Gardening, and Pest Control services).

The pack must include:

Business Card (front and back)
Envelope with recipient window on the right side (22x11)
A4 Letterhead

We provide:
Our final logo (PNG)
Three design references (Inspiration1, Inspiration2, Inspiration3) to spark ideas — but you are absolutely free to propose your own creative solutions based on these concepts.

What we want:
A clean, modern, and trustworthy style
A subtle but creative watermark or graphic detail on the letterhead (not too invasive)

The same visual "family feeling" across business card, envelope, and letterhead: designs must be different but clearly connected

Strong readability for all text and contact details

Use our brand colors (Navy Blue, Green, Orange/Red) in a smart, non-overloaded way

No strict limitations: we are open to creative proposals as long as they are coherent, elegant, and suitable for professional use

Technical specifications:
100% full A4 page layout (no accidental borders)

Deliver ready-to-print PDFs and vector files (AI, EPS)

Respect 5 mm safety margins

Standard sizes for A4, business card, envelope C6 with window at the right

Tone:
Modern – Clean – Elegant – Creative – Trustworthy

Target Market(s)

Professional businesses, property managers, condominium administrators, companies, clinics, and offices requiring cleaning, gardening, and pest control services. The design must convey trust, reliability, professionalism, and attention to detail.

Industry/Entity Type

Cleaning Services, Gardening Services, Pest Control Services

Colors
0054AA
0677BA
7BADD7
CADEEF
E8F1F8
59FF00
82FF00
B8FF75
E3FFCB
F4FFEA
EB3D1F
EC4F4E
F09395
F8D3D4
FCEDEE

Requirements
Must have
• Cohesive design across business card, letterhead, and envelope Clean, modern, professional look Use of brand colors: Navy Blue (main), Green, Orange/Red accents Letterhead must include a subtle watermark without interfering with text Envelope must be with a transparent window for recipient address visibility High readability of all text and contact details Proper alignment, no unnecessary margins (full A4 layout)
Nice to have
• Creative but discreet use of the checkmark from the logo as part of the background or watermark Slight variation or accent of color tones while respecting brand identity A clean visual accent that gives a sense of movement or dynamic professionalism (without being distracting) Icons for email, phone, and website on the business card (if stylistically appropriate)
Should not have
• Overuse of colors or rainbow effects Heavy backgrounds or complex textures that interfere with readability Fonts that are too playful, comic-style, or non-professional Overcrowded layouts — the design must feel clean and spacious Watermarks that are too strong or central (they must be subtle and marginal)

```html
<!DOCTYPE html>
<html lang="en">
<head>
<meta charset="utf-8">
<title>Velta Home – Corporate Identity</title>
<link href="https://fonts.googleapis.com/css2?family=DM+Sans:wght@400;500;700&display=swap" rel="stylesheet">
<style>
:root{
  --navy:#0c0872;
  --green:#6cc72e;
  --orange:#f26a1b;
  --ink:#1c1c1c;
  --paper:#ffffff;
  --backdrop:#ececec;
  --panel-top:#e9e9f4;
  --panel-bottom:#eff7e8;
}
*{margin:0;padding:0;box-sizing:border-box}
html,body{width:1200px;height:1058px;overflow:hidden;background:var(--backdrop);font-family:"DM Sans",sans-serif;color:var(--ink)}
.canvas{position:relative;width:1200px;height:1058px}
.piece{position:absolute;background:var(--paper);overflow:hidden;box-shadow:0 4px 14px rgba(0,0,0,.12)}
.abs{position:absolute}

.wordmark{display:flex;align-items:center;gap:7px;font-weight:700;color:var(--navy);letter-spacing:.02em;white-space:nowrap}
.wordmark .mark-square{background:var(--navy);display:block}
.wordmark.on-navy{color:#fff}
.wordmark.on-navy .mark-square{background:#fff}

.soft-panel{position:absolute;background:linear-gradient(160deg,var(--panel-top) 0%,var(--panel-top) 40%,var(--panel-bottom) 100%)}

.contact-list{list-style:none}
.contact-list li{display:flex;align-items:center;white-space:nowrap;color:var(--ink)}
.contact-list .ico{display:inline-flex;justify-content:center;align-items:center}
.tag{border:1px solid var(--orange);color:var(--orange);border-radius:6px;font-weight:700;line-height:1;text-align:center}
.web{color:var(--orange);font-weight:700;white-space:nowrap}
.company{color:var(--ink)}
.company b{font-weight:700}

/* plain footer band */
.base-band{position:absolute;left:0;right:0;bottom:0;background:var(--navy)}

/* Navy card front */
.card-front{left:256px;top:103px;width:259px;height:148px;background:var(--navy);color:#fff;text-align:center}
.card-front .wordmark{position:absolute;left:0;right:0;top:30px;justify-content:center;font-size:16px}
.card-front .mark-square{width:16px;height:16px}
.card-front .company{position:absolute;left:0;right:0;top:66px;font-size:8px;line-height:11.3px;color:#fff}

/* Small card back */
.card-back{left:256px;top:271px;width:259px;height:148px}
.card-back .soft-panel{left:118px;top:0;width:141px;height:141px}
.card-back .wordmark{left:21px;top:28px;font-size:15px}
.card-back .mark-square{width:14px;height:14px}
.card-back .person{left:21px;top:84px}
.card-back .person .name{font-size:10px;font-weight:700;color:var(--navy);letter-spacing:.01em}
.card-back .person .role{font-size:7px}
.card-back .contact-list{left:149px;top:76px;font-size:7.4px}
.card-back .contact-list li{height:11px;gap:5px}
.card-back .ico{width:11px}
.card-back .tag{font-size:4px;padding:1px 2px}
.card-back .web{left:148px;top:122px;font-size:7.4px}
.card-back .base-band{height:7px}

/* Large card */
.card-large{left:97px;top:463px;width:464px;height:232px}
.card-large .soft-panel{left:232px;top:0;width:232px;height:220px}
.card-large .wordmark{left:26px;top:40px;font-size:23px;gap:9px}
.card-large .mark-square{width:22px;height:22px}
.card-large .company{left:30px;top:135px;font-size:9.2px;line-height:12.2px}
.card-large .contact-list{left:245px;top:142px;font-size:9.2px}
.card-large .contact-list li{height:13px;gap:6px}
.card-large .ico{width:14px}
.card-large .tag{font-size:5px;padding:1px 2px}
.card-large .web{left:245px;top:198px;font-size:9.2px}
.card-large .base-band{height:12px}

/* Letterhead */
.letterhead{left:606px;top:62px;width:498px;height:700px}
.letterhead .soft-panel{left:312px;top:502px;width:186px;height:186px}
.letterhead .wordmark{left:30px;top:33px;font-size:20px;gap:9px}
.letterhead .mark-square{width:20px;height:20px}
.letterhead .company{left:297px;top:24px;font-size:8.8px;line-height:12.2px}
.letterhead .date{left:44px;top:169px;font-size:8.4px}
.letterhead .recipient{left:44px;top:189px;font-size:8.4px;line-height:11.5px}
.letterhead .recipient p+p{margin-top:6px}
.letterhead .salutation{left:44px;top:276px;font-size:10.5px;font-weight:500}
.letterhead .body{left:44px;top:297px;width:416px;font-size:8.1px;line-height:13.8px;text-align:justify}
.letterhead .body p+p{margin-top:8.3px}
.letterhead .signature{left:44px;top:533px;width:108px;height:28px;background:linear-gradient(90deg,#e6e6e6,#f3f3f3);border-radius:3px}
.letterhead .contact-col{top:632px;font-size:9px}
.letterhead .contact-col li{height:13px;gap:6px}
.letterhead .contact-col .ico{width:15px}
.letterhead .contact-col .tag{font-size:4.6px;padding:1px 2px}
.letterhead .col-a{left:44px}
.letterhead .col-b{left:179px}
.letterhead .web{left:44px;top:663px;font-size:9px}
.letterhead .base-band{height:12px}
</style>
</head>
<body>
<div class="canvas">

  <section class="piece card-front">
    <div class="wordmark on-navy"><span class="mark-square"></span>VELTA HOME</div>
    <div class="company">
      <b>Velta Home srl</b><br>
      <b>Societa unipersonale – Einzelunternehmen</b><br>
      Via dei Tigli – Lindenweg 8<br>
      I-39100 Valdoro-Goldtal (Bz)<br>
      REA – VWV Nr. Bz 317052<br>
      P.I.-MwSt. 04518830261
    </div>
  </section>

  <section class="piece card-back">
    <div class="soft-panel" role="img" aria-label="Soft lavender to green background accent"></div>
    <div class="wordmark abs"><span class="mark-square"></span>VELTA HOME</div>
    <div class="person abs">
      <div class="name">MARA KELLER</div>
      <div class="role">Director &amp; CEO</div>
    </div>
    <ul class="contact-list abs">
      <li><span class="ico"><svg width="7" height="7" viewBox="0 0 10 10"><path d="M2 0.5 L3.8 2.6 L2.8 3.8 Q4 6 6.2 7.2 L7.4 6.2 L9.5 8 L8.2 9.5 Q3.5 9 0.5 1.8 Z" fill="#f26a1b"/></svg></span>+39 333 5102847</li>
      <li><span class="ico"><svg width="7" height="6" viewBox="0 0 10 8"><rect width="10" height="8" rx="1" fill="#f26a1b"/><path d="M0.5 1 L5 4.5 L9.5 1" stroke="#fff" stroke-width="1" fill="none"/></svg></span>office@velta-home.srl</li>
      <li><span class="ico"><span class="tag">PEC</span></span>info.veltahome@pec.it</li>
      <li><span class="ico"><span class="tag">SDI</span></span>K7RTPB4</li>
    </ul>
    <div class="web abs">www.velta-home.srl</div>
    <div class="base-band"></div>
  </section>

  <section class="piece card-large">
    <div class="soft-panel" role="img" aria-label="Soft lavender to green background accent"></div>
    <div class="wordmark abs"><span class="mark-square"></span>VELTA HOME</div>
    <div class="company abs">
      <b>Velta Home srl</b><br>
      <b>Societa unipersonale – Einzelunternehmen</b><br>
      Via dei Tigli – Lindenweg 8<br>
      I-39100 Valdoro-Goldtal (Bz)<br>
      REA – VWV Nr. Bz 317052<br>
      P.I.-MwSt. 04518830261
    </div>
    <ul class="contact-list abs">
      <li><span class="ico"><svg width="9" height="9" viewBox="0 0 10 10"><path d="M2 0.5 L3.8 2.6 L2.8 3.8 Q4 6 6.2 7.2 L7.4 6.2 L9.5 8 L8.2 9.5 Q3.5 9 0.5 1.8 Z" fill="#f26a1b"/></svg></span>+39 333 5102847</li>
      <li><span class="ico"><svg width="9" height="7" viewBox="0 0 10 8"><rect width="10" height="8" rx="1" fill="#f26a1b"/><path d="M0.5 1 L5 4.5 L9.5 1" stroke="#fff" stroke-width="1" fill="none"/></svg></span>office@velta-home.srl</li>
      <li><span class="ico"><span class="tag">PEC</span></span>info.veltahome@pec.it</li>
      <li><span class="ico"><span class="tag">SDI</span></span>K7RTPB4</li>
    </ul>
    <div class="web abs">www.velta-home.srl</div>
    <div class="base-band"></div>
  </section>

  <section class="piece letterhead">
    <div class="soft-panel" role="img" aria-label="Subtle watermark background accent"></div>
    <div class="wordmark abs"><span class="mark-square"></span>VELTA HOME</div>
    <div class="company abs">
      <b>Velta Home srl</b><br>
      <b>Societa unipersonale – Einzelunternehmen</b><br>
      Via dei Tigli – Lindenweg 8<br>
      I-39100 Valdoro-Goldtal (Bz)<br>
      REA – VWV Nr. Bz 317052<br>
      P.I.-MwSt. 04518830261
    </div>
    <div class="date abs">30/12/2025</div>
    <div class="recipient abs">
      <p><b>Mara Keller</b><br>Director</p>
      <p>Lorem Ipsum Corp<br>Adress line here</p>
    </div>
    <div class="salutation abs">Ms Mara Keller</div>
    <div class="body abs">
      <p>Lorem ipsum dolor sit amet consectetur. Duis quis amet nunc vulputate dolor. Scelerisque ligula velit nulla faucibus donec pellentesque massa mi. Aliquam in fusce semper aliquam egestas mauris est nunc. Et pellentesque sodales elementum cursus mattis suscipit etiam nulla odio. Molestie tristique cursus ipsum non vitae nibh amet lacus. Orci dictum erat vitae at at non massa. Sit sit nisl pretium quisque ornare nunc posuere nunc. Et at est varius pulvinar sodales massa pulvinar risus. Orci at ipsum tellus posuere nunc.</p>
      <p>Auctor malesuada placerat scelerisque est. Sed tellus sit cras lectus risus ante. Scelerisque cursus risus sodales habitasse nibh volutpat. Eget libero aliquet hendrerit et tellus aliquam enim proin elementum. Enim purus nulla nunc accumsan suspendisse gravida dolor nulla. Eget diam elit rhoncus dui integer egestas. Eget sagittis tortor arcu id nec eu integer morbi risus. Posuere egestas ac penatibus imperdiet. Adipiscing rhoncus blandit tortor in. Tortor sagittis massa adipiscing in at nam placerat tincidunt.</p>
      <p>Massa etiam vel elementum varius in leo. Vitae id magna laoreet mauris. Sapien tellus sit blandit sit. Duis malesuada tristique purus aliquam orci blandit neque euismod viverra. Sit ut consectetur feugiat feugiat. Nec vitae sit ultrices eleifend semper justo tellus. Imperdiet tristique turpis mauris faucibus sed convallis porttitor. In rhoncus euismod at eget accumsan orci. Ac mattis libero interdum risus volutpat aliquam. Mauris auctor nulla sagittis vitae vulputate. Blandit mi enim amet a amet elementum tempor in.</p>
    </div>
    <div class="signature abs" role="img" aria-label="Handwritten signature of the director"></div>
    <ul class="contact-list contact-col col-a abs">
      <li><span class="ico"><svg width="9" height="9" viewBox="0 0 10 10"><path d="M2 0.5 L3.8 2.6 L2.8 3.8 Q4 6 6.2 7.2 L7.4 6.2 L9.5 8 L8.2 9.5 Q3.5 9 0.5 1.8 Z" fill="#f26a1b"/></svg></span>+39 333 5102847</li>
      <li><span class="ico"><svg width="9" height="7" viewBox="0 0 10 8"><rect width="10" height="8" rx="1" fill="#f26a1b"/><path d="M0.5 1 L5 4.5 L9.5 1" stroke="#fff" stroke-width="1" fill="none"/></svg></span>office@velta-home.srl</li>
    </ul>
    <ul class="contact-list contact-col col-b abs">
      <li><span class="ico"><span class="tag">PEC</span></span>info.veltahome@pec.it</li>
      <li><span class="ico"><span class="tag">SDI</span></span>K7RTPB4</li>
    </ul>
    <div class="web abs">www.velta-home.srl</div>
    <div class="base-band"></div>
  </section>

</div>
</body>
</html>
```